VELVET NUGGETS CANDY MYLAR BAG FILE SET UP FOR PRINT

☆6 FLAVORS
(It's ok to set up 1 flavor until the design is set then doing the rest of the flavors if it is easier)*
GREEN BAG
COMET TWIST
WATERMELON
PINK BAG
STRAWBERRY LEMONADE
PURPLE BAG
RIVER PLUM
LIGHT BLUE BAG
ZIP ZAP PLUM
BLUE BAG
BOLO FIZZY
☆Please Use the template (4"x6") , it is the correct size we need for the design.
INFORMATION FOR THE LABEL below
:::::
The FRONT/ BACK should be set up the same, any changes are below ::
THC
SUGAR
DROPS
SWEET & DELICIOUS VELVET FIZZ NUGGETS WITH MOUTHWATERING FLAVOR AND THC
10 PIECES PER PACKAGE - 200 MG THC TOTAL
on the back I need a small square candy with rounded corners with a dotted line down the middle . The candy should be about 1/4th the size of the taffy piece on the attached mylar)
10 MG THC = 1/2 PIECE
INGREDIENTS : CANE SUGAR, CONFECTIONERS GLUCOSE, WATER, THC EXTRACT, NATURAL & ARTIFICIAL FLAVORS & COLORS
ALLERGEN WARNING : MADE IN A FACILITY THAT HANDLES PEANUTS AND OTHER TREE NUTS.

```html
<!DOCTYPE html>
<html lang="en">
<head>
<meta charset="utf-8">
<title>Velvet Nuggets – River Plum Mylar Bag Front</title>
<link rel="stylesheet" href="https://fonts.googleapis.com/css2?family=Rubik:wght@900&family=Montserrat:wght@700&display=swap">
<style>
  :root {
    --backdrop: #d9d9d9;
    --bag-purple: #b0a8d4;
    --dieline-green: #1aa14a;
    --title-white: #ffffff;
    --title-glow: rgba(102, 80, 168, 0.55);
    --brand-pink: #e8a6d1;
    --badge-green: #0b6b2c;
  }
  * { margin: 0; padding: 0; box-sizing: border-box; }
  html, body {
    width: 1200px; height: 1200px; overflow: hidden;
    background: var(--backdrop);
  }
  .bag-front {
    position: absolute; left: 250px; top: 100px;
    width: 700px; height: 1000px;
    background: var(--bag-purple);
  }
  .dieline { position: absolute; inset: 0; }
  .compliance-badge {
    position: absolute; left: 512px; top: 236px;
    width: 104px; height: 104px;
    border-radius: 50%;
    background: var(--badge-green);
  }
  .title {
    position: absolute; left: 40px; right: 40px; top: 240px;
    text-align: center;
    font-family: "Rubik", sans-serif; font-weight: 900;
    color: var(--title-white);
    line-height: 1.02;
    letter-spacing: -1px;
    text-shadow: 0 4px 22px var(--title-glow);
  }
  .title .line-thc { font-size: 122px; display: block; margin-left: -10px; }
  .title .line-name { font-size: 94px; display: block; }
  .flavor {
    position: absolute; left: 40px; right: 40px; top: 596px;
    text-align: center;
    font-family: "Rubik", sans-serif; font-weight: 900;
    font-size: 64px; letter-spacing: 3px; word-spacing: 10px;
    color: var(--title-white);
    text-shadow: 0 3px 16px var(--title-glow);
  }
  .tagline {
    position: absolute; left: 40px; right: 40px; top: 698px;
    text-align: center;
    font-family: "Montserrat", sans-serif; font-weight: 700;
    font-size: 17px; line-height: 1.4; letter-spacing: 0.6px;
    color: var(--title-white);
  }
  .brand-name {
    position: absolute; left: 40px; right: 40px; top: 774px;
    text-align: center;
    font-family: "Rubik", sans-serif; font-weight: 900;
    font-size: 52px; line-height: 1.02;
    color: var(--brand-pink);
  }
  .dosage {
    position: absolute; left: 40px; right: 40px; top: 920px;
    text-align: center;
    font-family: "Montserrat", sans-serif; font-weight: 700;
    font-size: 17px; letter-spacing: 1px;
    color: var(--title-white);
  }
</style>
</head>
<body>
  <main class="bag-front">
    <svg class="dieline" width="700" height="1000" viewBox="0 0 700 1000" fill="none" stroke="var(--dieline-green)" stroke-width="2">
      <rect x="20" y="20" width="657" height="978" rx="32"/>
      <circle cx="349" cy="65" r="20"/>
      <line x1="20" y1="165" x2="677" y2="165"/>
      <line x1="20" y1="177" x2="677" y2="177"/>
      <g stroke-dasharray="14 9">
        <line x1="53" y1="20" x2="53" y2="965"/>
        <line x1="645" y1="20" x2="645" y2="965"/>
        <line x1="20" y1="130" x2="677" y2="130"/>
        <line x1="20" y1="213" x2="677" y2="213"/>
        <line x1="53" y1="965" x2="645" y2="965"/>
      </g>
      <path d="M20 98 L36 105 L20 112"/>
      <path d="M677 98 L661 105 L677 112"/>
    </svg>

    <div class="compliance-badge" role="img" aria-label="Regulatory product warning symbol"></div>

    <h1 class="title">
      <span class="line-thc">THC</span>
      <span class="line-name">VELVET</span>
      <span class="line-name">NUGGETS</span>
    </h1>

    <p class="flavor">RIVER PLUM</p>

    <p class="tagline">SWEET &amp; DELICIOUS VELVET FIZZ NUGGETS<br>WITH MOUTHWATERING FLAVOR AND THC</p>

    <p class="brand-name">FUZZY<br>LOAVES</p>

    <p class="dosage">10 PIECES PER PACKAGE - 200 MG THC TOTAL</p>
  </main>
</body>
</html>
```